NEW site with a tech flair and a feeling of moving forward!!

Hello Everyone,

We are starting with a small project to get the first 3-4 pages done. The winning designer will have an opportunity to work with us to design out the rest of the site. We estimate there will be between 15 and 20 total pages for the site (so there would probably be more work for the winner)!

We need a new website design to enhance the "coolness" factor of our brand image! Our current website is www.quillanmailworks.com and it needs some updating!

We envision a website where the homepage would be almost a landing page. It might have a 60 second video at the top, or a picture slider and contact info/site map at the bottom. In the middle we envision having the 3 service logos along with a quick summary of each service!

We have 3 main services: Tally Up, Shape Up and Send Off. We want to replace those names with our new service names which are: qUrgent, qPromoNet and qBlend-Up. Each service has its own unique logo! :)

If you look at www.quillanmailworks.com and notice the Tally Up / Shape Up / Send Off - - basically we are replacing those names with qUrgent / qPromoNet / and qBlend-Up. Then we just want to freshen things up - for example, the current information listed under "Tally Up" is "good" ...it just doesn't look "cool" ... we need a better way to display it. We provide complex services (and a lot of different services) and are hoping to make a new website that has a feel of being clean, modern, professional, with a technology flair and easy to use/understand our services.

The person visiting the website could watch the 60 second video to get an overview and then click on a logo for their desired service to be able to learn more. Once the user clicks a logo for the desired service, a new page would open and the user could then learn about the service.

After submitting a design for the homepage, please work on a design to totally revamp the "Tally Up" page. We don't like the way that is laid out and need to freshen it up. Note: the layout we choose for Tally Up will be similar for Send Off and Shape Up.

The perfect website will have a combo of a technology flair, a feeling of moving forward and/or of connecting people/things/information together. The website should convey trust.

ABOUT QUILLAN MAILWORKS

We are a technology and communications company. We receive data files, print, fold, insert and mail invoices, statements and other important notices. We also deliver via email, SMS/Text Message and IVR Phone calls. Finally we offer an online website where customers can go to pay their invoices. It is important that the website have a clean, modern, professional and technology look/feel.

We also provide marketing and advertising services through the mail and digitally.

**Please note, our main company is called Quillan Mailworks...we have uploaded our 2 new logos (for your reference) for qUrgent and qPromoNet for reference.

Please message me with any questions! Thanks everyone, looking forward to seeing the designs!

Target Market(s)

Financial companies, Healthcare and Utilities.

Industry/Entity Type

Tech

Number of Pages Required

5+ page

Requirements
Must have
• The perfect website will have a combo of a technology flair, a feeling of moving forward and/or of connecting people/things/information together. The website should convey trust.
Nice to have
• Taking our complicated services and products and making them really simple and easy to understand by using graphs, charts, pictures and other illustrations.
• Eye catchy feel. Needs to be simple. Conveys trustworthy feel.
Should not have
• Can't be boring and bland. Can't be too complex.

```html
<!DOCTYPE html>
<html lang="en">
<head>
<meta charset="utf-8">
<title>Quillan Mailworks</title>
<link href="https://fonts.googleapis.com/css2?family=Open+Sans:wght@400;600;700&family=Montserrat:wght@500;600;700&display=swap" rel="stylesheet">
<style>
:root{
  --blue:#2a8fd0;
  --navy:#16578f;
  --deep:#0f4778;
  --sky:#5fb3e3;
  --foot:#3f9ad6;
  --ink:#4a5560;
  --muted:#7d8791;
  --white:#ffffff;
  --bar:#2f7fb9;
}
*{margin:0;padding:0;box-sizing:border-box}
html,body{width:742px;height:1200px;overflow:hidden;background:#fff}
body{font-family:"Open Sans",Arial,sans-serif;color:var(--ink);position:relative}
.header{height:62px;position:relative;background:#fff}
.header-brand{position:absolute;left:80px;top:24px;display:flex;align-items:center;gap:6px}
.brand-dot{width:11px;height:11px;border-radius:50%;background:var(--blue);flex:none}
.brand-name{font-weight:700;font-size:16px;color:var(--navy);white-space:nowrap}
.utility{position:absolute;right:38px;top:5px;display:flex;gap:20px;font-size:7px;color:var(--muted);text-transform:uppercase}
.nav{position:absolute;right:38px;top:30px;display:flex;gap:3px}
.nav a{font-family:"Montserrat",sans-serif;font-size:7.5px;font-weight:600;color:var(--navy);text-decoration:none;padding:7px 8px;text-transform:uppercase}
.nav a.active{background:var(--blue);color:#fff}
.hero{position:absolute;top:62px;left:0;width:742px;height:362px;background:linear-gradient(120deg,#c9d6df 0%,#e8edf1 40%,#9fb0bf 75%,#6e8396 100%)}
.play{position:absolute;left:346px;top:155px;width:52px;height:44px;background:var(--blue);border-radius:4px;display:flex;align-items:center;justify-content:center}
.hero-title{position:absolute;right:86px;top:270px;font-family:"Montserrat",sans-serif;font-weight:700;font-size:20px;line-height:26px;color:#fff;text-align:right;text-shadow:0 1px 3px rgba(0,0,0,.3)}
.services{position:absolute;top:450px;left:0;width:742px;text-align:center}
.section-title{font-family:"Montserrat",sans-serif;font-weight:700;font-size:18px;color:var(--navy)}
.rule{width:60px;height:2px;background:var(--blue);margin:8px auto 0}
.cards{display:flex;justify-content:center;gap:40px;margin-top:46px}
.card{width:150px;text-align:center}
.card-logo{font-family:"Montserrat",sans-serif;font-weight:600;font-size:20px;color:var(--navy);height:36px;display:flex;align-items:center;justify-content:center;gap:6px;white-space:nowrap}
.card-logo span{width:9px;height:9px;background:var(--blue);border-radius:50%}
.card p{font-size:9px;line-height:13px;color:var(--muted);margin-top:20px;height:40px}
.btn{display:inline-block;margin-top:20px;background:var(--blue);color:#fff;font-size:8px;font-weight:700;padding:7px 14px;text-transform:uppercase;letter-spacing:.4px}
.about-band{position:absolute;top:700px;left:0;width:742px;height:150px}
.about-title{position:absolute;top:782px;left:82px;font-family:"Montserrat",sans-serif;font-weight:700;font-size:18px;color:#fff}
.about-text{position:absolute;top:848px;left:82px;width:580px;font-size:9.5px;line-height:15px;color:var(--ink)}
.about-text p+p{margin-top:16px}
.footer{position:absolute;top:950px;left:0;width:742px;height:250px}
.foot-inner{position:absolute;top:1000px;left:80px;width:640px;display:flex;color:#fff;font-size:8.5px}
.foot-brand{width:190px}
.foot-logo{display:flex;align-items:center;gap:6px;margin-top:4px}
.foot-logo .brand-dot{background:#fff}
.foot-logo .brand-name{color:#fff;font-size:15px}
.follow{margin-top:40px;font-size:8px;font-weight:700;text-transform:uppercase;padding-left:34px}
.socials{display:flex;gap:8px;margin-top:8px;padding-left:28px}
.socials span{width:18px;height:18px;border-radius:50%;background:var(--navy)}
.col h4{font-size:8px;font-weight:700;text-transform:uppercase;margin-bottom:12px}
.menu{width:90px}
.menu li{list-style:none;line-height:16px}
.news{width:180px}
.news-form .field{width:96px;height:24px;background:#fff;color:var(--muted);font-size:8px;padding:6px 8px}
.news-form .go{display:inline-block;background:var(--navy);color:#fff;font-size:8px;font-weight:700;padding:7px 10px;margin-left:104px;margin-top:8px}
.contact{width:170px}
.contact p{line-height:12px;margin-bottom:12px}
.copy{position:absolute;bottom:0;left:0;width:742px;height:24px;background:var(--bar);color:#dbe9f5;font-size:7px;text-align:center;line-height:24px}
</style>
</head>
<body>
<header class="header">
  <div class="header-brand"><span class="brand-dot"></span><span class="brand-name">Quillan Mailworks</span></div>
  <div class="utility"><span>(555) 014-2286</span><span>Home</span><span>Email</span><span>Contact</span></div>
  <nav class="nav">
    <a class="active">Home</a><a>qUrgent</a><a>qPromoNet</a><a>qBlend-Up</a><a>Security</a><a>Industries</a><a>Pay Bills</a>
  </nav>
</header>

<section class="hero" role="img" aria-label="Photo of people working at a laptop in an office">
  <div class="play"><svg width="18" height="20" viewBox="0 0 18 20"><path d="M2 1 L17 10 L2 19 Z" fill="#fff"/></svg></div>
  <h1 class="hero-title">TECHNOLOGY AND<br>COMMUNICATIONS</h1>
</section>

<section class="services">
  <h2 class="section-title">OUR SERVICES</h2>
  <div class="rule"></div>
  <div class="cards">
    <div class="card"><div class="card-logo"><span></span>qUrgent</div><p>It is a long established fact that a reader will be distracted by the readable content of a page when.</p><a class="btn">Read more ›</a></div>
    <div class="card"><div class="card-logo"><span></span>qPromoNet</div><p>On the other hand, we denounce with righteous indignation and dislike men who are so beguiled.</p><a class="btn">Read more ›</a></div>
    <div class="card"><div class="card-logo"><span></span>qBlend-Up</div><p>At vero eos et accusamus et iusto odio dignissimos ducimus qui blanditiis praesentium voluptatum.</p><a class="btn">Read more ›</a></div>
  </div>
</section>

<svg class="about-band" viewBox="0 0 742 150" preserveAspectRatio="none">
  <polygon points="0,50 742,0 742,30 0,120" fill="#5fb3e3"/>
  <polygon points="0,60 742,20 742,110 0,125" fill="#16578f"/>
</svg>
<h2 class="about-title">ABOUT US</h2>
<div class="about-text">
  <p>We are a technology and communications company. We receive data files, print, fold, insert and mail invoices, statements and other important notices. We also deliver via email, SMS/Text Message and IVR Phone calls. Finally we offer an online website where customers can go to pay their invoices. It is important that the website have a clean, modern, professional and technology look/feel.</p>
  <p>We also provide marketing and advertising services through the mail and digitally.</p>
</div>

<svg class="footer" viewBox="0 0 742 250" preserveAspectRatio="none">
  <polygon points="0,30 742,0 742,250 0,250" fill="#3f9ad6"/>
  <polygon points="0,30 742,0 742,6 0,38" fill="#7cc3ea"/>
</svg>
<div class="foot-inner">
  <div class="foot-brand">
    <div class="foot-logo"><span class="brand-dot"></span><span class="brand-name">Quillan Mailworks</span></div>
    <div class="follow">Follow us</div>
    <div class="socials"><span></span><span></span><span></span></div>
  </div>
  <div class="col menu"><h4>Menu</h4><ul><li>Security</li><li>Industries</li><li>Pay Bills</li><li>Careers</li><li>About Us</li><li>Contact Us</li></ul></div>
  <div class="col news"><h4>Newsletter</h4><div class="news-form"><div class="field">Email</div><div class="go">SIGNUP</div></div></div>
  <div class="col contact"><h4>Contact us</h4><p>Quillan Mailworks, Inc.<br>2140 Harbor Loop Dr<br>Ashford, OR 97310</p><p>(555) 014-2286</p><p>hello@quillanmailworks.com</p></div>
</div>
<div class="copy">Copyright 2016 © All rights reserved.</div>
</body>
</html>
```